Long term design collaboration - mobile app design & web app design

We are looking for a talented mobile designer to help us improve our UI & UX for mobile app and web app.

The screens that need to be redesigned are attached.

There is potentially a lot more work in future design available for the successful candidate.
The successful candidate would have to take part in daily stand-up around 3 times per week.
The successful candidate would join a dev team
We are software company that does property management

```html
<!DOCTYPE html>
<html lang="en">
<head>
<meta charset="utf-8">
<title>Hestia – Mobile &amp; Web Screens</title>
<link href="https://fonts.googleapis.com/css2?family=Inter:wght@400;500;600;700&family=Outfit:wght@500;600&display=swap" rel="stylesheet">
<style>
:root{
  --page:#f2f2f2;
  --ink:#1d1e22;
  --muted:#9a9ca4;
  --blue:#2a57c9;
  --blue-soft:#e9eefb;
  --soft:#f5f6f8;
  --line:#e8e9ed;
  --screen:#ffffff;
  --canvas:#f4f5f7;
  --warn:#f5a524;
  --warn-soft:#fff2da;
  --red:#e03131;
  --red-soft:#fdeaea;
  --green:#7fdc87;
  --edge:#d8d9de;
}
*{box-sizing:border-box}
html,body{margin:0;width:1027px;height:1200px;overflow:hidden}
body{background:var(--page);font-family:"Inter",sans-serif;color:var(--ink);position:relative}
svg.ic{width:6px;height:6px;display:block;flex:none}
.title{position:absolute;top:92px;margin:0;font-family:"Outfit",sans-serif;font-weight:600;font-size:28px;letter-spacing:.5px;color:#7a7a7c}
.label{position:absolute;top:138px;margin:0;font-size:5.6px;font-weight:600}

/* phones */
.phone{position:absolute;background:var(--screen);border:1px solid var(--edge);border-radius:10px;overflow:hidden;display:flex;flex-direction:column}
.status{height:12px;flex:none;display:flex;justify-content:space-between;align-items:center;padding:0 7px;font-size:3.1px}
.status .sys{display:flex;gap:1.5px;align-items:center}
.status .sys i{display:block;background:currentColor;border-radius:.5px}
.bar{height:16px;flex:none;display:flex;align-items:center;gap:7px;padding:0 7px;border-bottom:1px solid var(--line)}
.bar h2{margin:0;font-size:4.8px;font-weight:600}
.bar .ic{width:5px;height:5px}
.pbody{padding:0 6px;flex:1}
.sec{text-align:center;font-size:4.1px;font-weight:500;margin:7px 0 5px}
.row{display:flex;align-items:center;gap:5px;background:var(--soft);border-radius:3px;padding:4px;margin-bottom:3px}
.tile{width:12px;height:12px;border-radius:3.5px;background:var(--blue-soft);color:var(--blue);display:grid;place-items:center;flex:none}
.tile .ic{width:6px;height:6px}
.tile.warn{background:var(--warn-soft);color:var(--warn)}
.tile.red{background:var(--red-soft);color:var(--red)}
.txt{flex:1;display:flex;flex-direction:column;gap:1.6px}
.txt b{font-size:3.5px;font-weight:500}
.txt small{font-size:2.7px;color:var(--muted);line-height:1.4}
.go{width:5px;height:5px;border-radius:50%;background:#ebecef;color:#a6a8ae;display:grid;place-items:center;flex:none}
.go .ic{width:3px;height:3px}
.tabs{margin-top:auto;height:26px;flex:none;display:flex;justify-content:space-around;align-items:center;border-top:1px solid var(--line);color:#b3b5bb}
.tabs span{display:flex;flex-direction:column;align-items:center;gap:2px;font-size:2.8px}
.tabs .ic{width:6.5px;height:6.5px}
.tabs .on{color:var(--blue)}
.group{border:1px solid var(--line);border-radius:3px;padding:4px;margin-bottom:4px;background:#fff}
.ghead{display:flex;justify-content:space-between;align-items:center;font-size:3.2px;margin-bottom:4px}
.stats{display:flex;gap:4px}
.stat{flex:1;background:var(--soft);border-radius:3px;padding:3px 4px;display:flex;align-items:center;gap:4px}
.stat .ic{width:7px;height:7px;color:var(--blue)}
.stat div{display:flex;flex-direction:column;gap:1px}
.stat small{font-size:2.5px;color:var(--muted)}
.stat strong{font-size:3.8px;font-weight:600}
.q{text-align:center;font-size:4px;font-weight:500;margin:9px 0 7px}
.opt{display:flex;align-items:center;gap:5px;background:var(--soft);border-radius:3px;padding:0 5px;height:15px;margin-bottom:5px;font-size:3.1px}
.radio{width:6px;height:6px;border-radius:50%;background:#e6e7eb;flex:none;display:grid;place-items:center;color:#fff}
.radio.on{background:var(--blue)}
.radio .ic{width:3.5px;height:3.5px}
.btns{display:flex;gap:5px;padding:0 6px 12px}
.btn{flex:1;height:12px;border-radius:2.5px;display:grid;place-items:center;font-size:3.3px;font-weight:500;border:1px solid var(--line);background:#fff}
.btn.primary{background:var(--blue);color:#fff;border-color:var(--blue)}

/* option two phones */
.phone.blue{background:var(--canvas)}
.bluehead{background:var(--blue);color:#fff;flex:none}
.bluehead .bar{border:0;height:20px}
.bluehead .back{width:7px;height:7px;border-radius:50%;background:#fff;color:var(--blue);display:grid;place-items:center}
.bluehead .back .ic{width:4px;height:4px}
.grid2{display:grid;grid-template-columns:1fr 1fr;gap:5px}
.gcard{background:#fff;border-radius:3px;padding:5px;position:relative;min-height:36px;display:flex;flex-direction:column;gap:2px}
.gcard .tile{width:11px;height:11px;margin-bottom:3px}
.gcard .tile.fill{background:var(--blue-soft)}
.gcard b{font-size:3.4px;font-weight:500}
.gcard small{font-size:2.6px;color:var(--muted);line-height:1.4;padding-right:6px}
.gcard .go{position:absolute;right:3px;bottom:3px;background:var(--blue-soft)}
.navicons{margin-top:auto;height:22px;flex:none;background:#fff;display:flex;justify-content:space-around;align-items:center;color:#c9cbd0}
.navicons .ic{width:6px;height:6px}
.navicons .on{width:12px;height:12px;border-radius:50%;background:var(--blue-soft);color:var(--blue);display:grid;place-items:center}
.stat.col{flex-direction:column;align-items:flex-start;gap:4px;background:var(--soft)}
.stat.col .top{display:flex;gap:3px;align-items:center}
.opt2{display:flex;align-items:center;gap:5px;background:#fff;border-radius:3px;padding:0 5px;min-height:14px;margin-bottom:5px;font-size:3.1px;line-height:1.5}
.opt2 .mark{width:7px;height:7px;flex:none}
.opt2 .radio{margin-left:auto}

/* tablets */
.tab{position:absolute;background:#fff;border:1px solid var(--edge);border-radius:9px;overflow:hidden;display:flex;flex-direction:column}
.top{height:22px;flex:none;display:flex;align-items:center;border-bottom:1px solid var(--line)}
.brand{font-size:5.4px;color:var(--blue);font-weight:500;margin-left:8px}
.menu-btn{color:var(--blue);width:7px;height:7px;margin-left:10px}
.sidehead{height:100%;display:flex;align-items:center;gap:5px;padding:0 6px 0 8px;border-right:1px solid var(--line);font-size:3.4px;color:var(--blue)}
.sidehead .close{margin-left:auto;width:5px;height:5px}
.user{margin-left:auto;margin-right:9px;display:flex;align-items:center;gap:5px}
.bell{width:8px;height:8px;border-radius:50%;background:var(--blue-soft);color:var(--blue);display:grid;place-items:center;margin-right:4px}
.bell .ic{width:4.5px;height:4.5px}
.avatar{width:11px;height:11px;border-radius:50%;background:radial-gradient(circle at 45% 40%,#c9a98a,#6b5444)}
.who{display:flex;flex-direction:column;gap:1px}
.who b{font-size:3.4px;font-weight:600}
.who small{font-size:2.8px;color:#c3c5cb}
.body{flex:1;display:flex;min-height:0}
.rail{width:25px;flex:none;display:flex;flex-direction:column;align-items:center;gap:8px;padding:8px 0 10px;color:#a8abb2;border-right:1px solid var(--line)}
.rail .ic{width:6px;height:6px}
.rail .act{width:11px;height:11px;border-radius:3px;background:var(--blue);color:#fff;display:grid;place-items:center}
.rail .end{margin-top:auto}
.menu{width:67px;flex:none;border-right:1px solid var(--line);display:flex;flex-direction:column;padding:4px 0 8px}
.menu a{display:flex;align-items:center;gap:5px;padding:0 8px;height:17px;font-size:3.4px;color:#4a4c52;text-decoration:none}
.menu a .ic{width:5.5px;height:5.5px;color:#666}
.menu a.on{background:var(--blue-soft);color:var(--blue)}
.menu a.on .ic{color:var(--blue)}
.menu .end{margin-top:auto;color:#b3b5bb}
.main{flex:1;background:var(--canvas);padding:3px 9px 6px;min-width:0}
.ovhead{display:flex;justify-content:space-between;align-items:center;margin:3px 0 6px}
.ovhead h2{margin:0;font-size:4.6px;font-weight:500}
.report{width:28px;height:10px;border-radius:2px;background:var(--blue);color:#fff;font-size:3.3px;display:grid;place-items:center}
.banner{background:#fff;border-radius:3px;padding:4px 6px 5px}
.notice{display:flex;align-items:center;gap:4px;font-size:3.3px;color:#6a6c72;margin-bottom:5px}
.notice i{width:4px;height:4px;border-radius:50%;background:var(--warn)}
.chips{display:flex;gap:5px}
.chip{flex:1;height:9px;border:1px solid var(--line);border-radius:2px;display:flex;align-items:center;justify-content:space-between;padding:0 3px;font-size:3.1px;color:#6a6c72;white-space:nowrap}
.chip .ic{width:3px;height:3px}
.tabsbar{background:#fff;border-radius:3px;padding:2px;margin:5px 0;display:flex;gap:8px;align-items:center;font-size:3.2px;color:var(--muted)}
.pill{width:32px;height:8px;border-radius:2px;background:var(--blue);color:#fff;display:grid;place-items:center}
.block{background:#fff;border-radius:3px;padding:4px 5px 5px;margin-bottom:5px}
.block h4{margin:0 0 4px;font-size:3.6px;font-weight:500}
.cells{display:flex;gap:5px}
.cell{flex:1;background:var(--soft);border-radius:3px;height:22px;padding:3px 4px;display:flex;flex-direction:column;justify-content:space-between}
.cells.fixed .cell{flex:none;width:calc((100% - 20px)/5)}
.cell .lab{display:flex;align-items:center;gap:3px;font-size:2.8px;color:var(--muted)}
.cell .lab .ic{width:4.5px;height:4.5px;color:var(--blue)}
.cell .lab .go{margin-left:auto;width:4px;height:4px;background:#fff}
.cell .val{font-size:3.4px;white-space:nowrap}
.fin h2{margin:9px 0 6px;font-size:4.3px;font-weight:500}
.fcards{display:flex;gap:8px}
.fcard{width:48px;height:42px;background:#fff;border-radius:3px;display:flex;flex-direction:column;align-items:center;justify-content:center;gap:3px;font-size:3.3px;color:#6a6c72}
.fcard .ic{width:10px;height:10px;color:var(--blue)}
.fcard .foot{display:flex;gap:3px;align-items:center}
.ok{height:5px;padding:0 5px;border-radius:3px;background:var(--green);font-size:2.6px;color:#2d6b34;display:grid;place-items:center}
.fchips{display:flex;gap:6px}
.fchip{height:12px;background:#fff;border-radius:3px;display:flex;align-items:center;gap:4px;padding:0 4px;font-size:3.3px;color:#6a6c72}
.fchip .ic{width:7px;height:7px;color:var(--blue)}
.rail.tall{gap:0;padding-top:6px;width:22px}
.rail.tall .ic{margin:3.6px 0}
.menu.long a{height:13.2px}
</style>
</head>
<body>

<svg width="0" height="0" style="position:absolute" aria-hidden="true">
  <symbol id="i-doc" viewBox="0 0 16 16"><rect x="3" y="2" width="10" height="12" rx="2" fill="none" stroke="currentColor" stroke-width="1.6"/><path d="M6 6h4M6 9h4" stroke="currentColor" stroke-width="1.6"/></symbol>
  <symbol id="i-cal" viewBox="0 0 16 16"><rect x="2" y="3" width="12" height="11" rx="2" fill="none" stroke="currentColor" stroke-width="1.6"/><path d="M2 7h12M5 1.5v3M11 1.5v3" stroke="currentColor" stroke-width="1.6"/></symbol>
  <symbol id="i-layers" viewBox="0 0 16 16"><path d="M8 2l6 3-6 3-6-3z" fill="none" stroke="currentColor" stroke-width="1.5" stroke-linejoin="round"/><path d="M2 8l6 3 6-3M2 11l6 3 6-3" fill="none" stroke="currentColor" stroke-width="1.5" stroke-linejoin="round"/></symbol>
  <symbol id="i-pin" viewBox="0 0 16 16"><path d="M8 15s5-5 5-8.5A5 5 0 003 6.5C3 10 8 15 8 15z" fill="none" stroke="currentColor" stroke-width="1.6"/><circle cx="8" cy="6.5" r="1.8" fill="currentColor"/></symbol>
  <symbol id="i-cash" viewBox="0 0 16 16"><rect x="1.5" y="4" width="13" height="8" rx="1.5" fill="none" stroke="currentColor" stroke-width="1.6"/><circle cx="8" cy="8" r="2" fill="none" stroke="currentColor" stroke-width="1.6"/></symbol>
  <symbol id="i-alert" viewBox="0 0 16 16"><circle cx="8" cy="8" r="6" fill="none" stroke="currentColor" stroke-width="1.6"/><path d="M8 4.5v4.5" stroke="currentColor" stroke-width="1.8"/><circle cx="8" cy="11.3" r="1" fill="currentColor"/></symbol>
  <symbol id="i-help" viewBox="0 0 16 16"><circle cx="8" cy="8" r="6" fill="none" stroke="currentColor" stroke-width="1.6"/><path d="M6.2 6.3a1.9 1.9 0 113 1.6c-.8.5-1.2.9-1.2 1.7" fill="none" stroke="currentColor" stroke-width="1.5"/><circle cx="8" cy="11.6" r=".9" fill="currentColor"/></symbol>
  <symbol id="i-chev" viewBox="0 0 16 16"><path d="M6 3.5l4.5 4.5L6 12.5" fill="none" stroke="currentColor" stroke-width="2" stroke-linecap="round" stroke-linejoin="round"/></symbol>
  <symbol id="i-back" viewBox="0 0 16 16"><path d="M10 3.5L5.5 8l4.5 4.5" fill="none" stroke="currentColor" stroke-width="2" stroke-linecap="round" stroke-linejoin="round"/></symbol>
  <symbol id="i-x" viewBox="0 0 16 16"><path d="M4 4l8 8M12 4l-8 8" stroke="currentColor" stroke-width="2" stroke-linecap="round"/></symbol>
  <symbol id="i-tick" viewBox="0 0 16 16"><path d="M3.5 8.5l3 3 6-7" fill="none" stroke="currentColor" stroke-width="2.4" stroke-linecap="round" stroke-linejoin="round"/></symbol>
  <symbol id="i-home" viewBox="0 0 16 16"><path d="M2.5 7L8 2.5 13.5 7v6.5h-4v-4h-3v4h-4z" fill="none" stroke="currentColor" stroke-width="1.6" stroke-linejoin="round"/></symbol>
  <symbol id="i-pie" viewBox="0 0 16 16"><path d="M7 3a5.5 5.5 0 105.5 5.5H7z" fill="none" stroke="currentColor" stroke-width="1.6"/><path d="M9.5 1.5v5h5a5 5 0 00-5-5z" fill="none" stroke="currentColor" stroke-width="1.6"/></symbol>
  <symbol id="i-coin" viewBox="0 0 16 16"><circle cx="8" cy="8" r="6" fill="none" stroke="currentColor" stroke-width="1.6"/><path d="M9.8 5.5H7.3a1.3 1.3 0 000 2.6h1.4a1.3 1.3 0 010 2.6H6.2M8 4v1.5M8 10.7v1.5" fill="none" stroke="currentColor" stroke-width="1.3"/></symbol>
  <symbol id="i-mail" viewBox="0 0 16 16"><rect x="2" y="3.5" width="12" height="9" rx="1.5" fill="none" stroke="currentColor" stroke-width="1.6"/><path d="M2.5 4.5L8 9l5.5-4.5" fill="none" stroke="currentColor" stroke-width="1.6"/></symbol>
  <symbol id="i-bell" viewBox="0 0 16 16"><path d="M4 11V7.5a4 4 0 018 0V11l1.5 1.5h-11z" fill="none" stroke="currentColor" stroke-width="1.6" stroke-linejoin="round"/><path d="M6.5 14h3" stroke="currentColor" stroke-width="1.6"/></symbol>
  <symbol id="i-menu" viewBox="0 0 16 16"><path d="M2 4h12M2 8h12M2 12h12" stroke="currentColor" stroke-width="1.8" stroke-linecap="round"/></symbol>
  <symbol id="i-user" viewBox="0 0 16 16"><circle cx="8" cy="5.5" r="3" fill="none" stroke="currentColor" stroke-width="1.4"/><path d="M2.5 14.5a5.5 5.5 0 0111 0z" fill="none" stroke="currentColor" stroke-width="1.4"/></symbol>
  <symbol id="i-globe" viewBox="0 0 16 16"><circle cx="8" cy="8" r="6" fill="none" stroke="currentColor" stroke-width="1.4"/><path d="M2 8h12M8 2c2 2 2 10 0 12M8 2c-2 2-2 10 0 12" fill="none" stroke="currentColor" stroke-width="1.2"/></symbol>
  <symbol id="i-building" viewBox="0 0 16 16"><path d="M3 14V3h6v11M9 7h4v7M1.5 14h13M5 6h2M5 9h2" fill="none" stroke="currentColor" stroke-width="1.5"/></symbol>
  <symbol id="i-bank" viewBox="0 0 16 16"><path d="M2 6l6-3.5L14 6zM3.5 7v5M6.5 7v5M9.5 7v5M12.5 7v5M2 13.5h12" fill="none" stroke="currentColor" stroke-width="1.4" stroke-linejoin="round"/></symbol>
  <symbol id="i-folder" viewBox="0 0 16 16"><path d="M2 4.5h4.5l1.5 1.5h6v7H2z" fill="none" stroke="currentColor" stroke-width="1.5" stroke-linejoin="round"/></symbol>
  <symbol id="i-gear" viewBox="0 0 16 16"><circle cx="8" cy="8" r="2.2" fill="none" stroke="currentColor" stroke-width="1.5"/><circle cx="8" cy="8" r="5.5" fill="none" stroke="currentColor" stroke-width="1.5" stroke-dasharray="2.2 1.4"/></symbol>
  <symbol id="i-drop" viewBox="0 0 16 16"><path d="M8 2s4.5 5 4.5 8a4.5 4.5 0 01-9 0C3.5 7 8 2 8 2z" fill="none" stroke="currentColor" stroke-width="1.6"/></symbol>
  <symbol id="i-wrench" viewBox="0 0 16 16"><path d="M10.5 2a3.5 3.5 0 00-3.2 4.8L2.5 11.6l1.9 1.9 4.8-4.8A3.5 3.5 0 0014 5.5l-2 2-2-2 2-2A3.5 3.5 0 0010.5 2z" fill="none" stroke="currentColor" stroke-width="1.3" stroke-linejoin="round"/></symbol>
  <symbol id="i-refresh" viewBox="0 0 16 16"><path d="M3 8a5 5 0 109-3M12 2v3H9" fill="none" stroke="currentColor" stroke-width="1.6" stroke-linecap="round"/></symbol>
  <symbol id="i-logout" viewBox="0 0 16 16"><path d="M9 2.5H3.5v11H9M7 8h7M11.5 5.5L14 8l-2.5 2.5" fill="none" stroke="currentColor" stroke-width="1.5" stroke-linejoin="round"/></symbol>
  <symbol id="i-key" viewBox="0 0 16 16"><circle cx="8" cy="5" r="3" fill="none" stroke="currentColor" stroke-width="1.5"/><path d="M8 8v6M8 11h2M8 13h2" stroke="currentColor" stroke-width="1.5"/></symbol>
  <symbol id="i-ruler" viewBox="0 0 16 16"><path d="M2.5 2.5v11h11zM5 9.5v2h2" fill="none" stroke="currentColor" stroke-width="1.5" stroke-linejoin="round"/></symbol>
  <symbol id="i-no" viewBox="0 0 16 16"><circle cx="8" cy="8" r="7" fill="#e5383b"/><path d="M3.5 3.5l9 9" stroke="#fff" stroke-width="2"/></symbol>
  <symbol id="i-file-y" viewBox="0 0 16 16"><path d="M3 1.5h7l3 3v10H3z" fill="#f5b72e"/><path d="M5.5 7h5M5.5 10h5" stroke="#fff" stroke-width="1.2"/><circle cx="12.5" cy="12.5" r="2.5" fill="#e5383b"/></symbol>
  <symbol id="i-file-b" viewBox="0 0 16 16"><path d="M3 1.5h7l3 3v10H3z" fill="#2a57c9"/><path d="M5.5 7h5M5.5 10h5" stroke="#fff" stroke-width="1.2"/><circle cx="12.5" cy="12.5" r="2.5" fill="#f5b72e"/></symbol>
</svg>

<h1 class="title" style="left:86px">OPTION ONE</h1>
<h1 class="title" style="left:561px">OPTION TWO</h1>

<p class="label" style="left:90px">Development Overview</p>
<p class="label" style="left:217px">Finances</p>
<p class="label" style="left:353px">Legionellas</p>
<p class="label" style="left:565px">Development Overview</p>
<p class="label" style="left:714px">Finances</p>
<p class="label" style="left:863px">Legionellas</p>

<!-- Option one: development overview -->
<section class="phone" style="left:87px;top:157px;width:110px;height:288px">
  <div class="status"><span>12:30PM</span><span class="sys"><i style="width:2.5px;height:2.5px"></i><i style="width:2.5px;height:2.5px;border-radius:50%"></i><i style="width:4px;height:2.2px"></i></span></div>
  <header class="bar"><svg class="ic"><use href="#i-back"/></svg><h2>Development Overview</h2></header>
  <div class="pbody">
    <h3 class="sec">General</h3>
    <div class="row"><span class="tile"><svg class="ic"><use href="#i-cal"/></svg></span><div class="txt"><b>Handover Date</b><small>12 January 2023</small></div><span class="go"><svg class="ic"><use href="#i-chev"/></svg></span></div>
    <div class="row"><span class="tile"><svg class="ic"><use href="#i-layers"/></svg></span><div class="txt"><b>Units</b><small>85</small></div><span class="go"><svg class="ic"><use href="#i-chev"/></svg></span></div>
    <div class="row"><span class="tile"><svg class="ic"><use href="#i-pin"/></svg></span><div class="txt"><b>Address</b><small>24 Alder Row,<br>Northfield, NF2 8QA</small></div><span class="go"><svg class="ic"><use href="#i-chev"/></svg></span></div>
    <div class="row"><span class="tile"><svg class="ic"><use href="#i-cash"/></svg></span><div class="txt"><b>Section 20 limit</b><small>£ 20</small></div><span class="go"><svg class="ic"><use href="#i-chev"/></svg></span></div>
    <h3 class="sec">Compliance</h3>
    <div class="row"><span class="tile"><svg class="ic"><use href="#i-doc"/></svg></span><div class="txt"><b>Asbestos</b><small>NA</small></div><span class="go"><svg class="ic"><use href="#i-chev"/></svg></span></div>
    <div class="row"><span class="tile warn"><svg class="ic"><use href="#i-help"/></svg></span><div class="txt"><b>EICR</b><small>-</small></div><span class="go"><svg class="ic"><use href="#i-chev"/></svg></span></div>
    <div class="row"><span class="tile red"><svg class="ic"><use href="#i-alert"/></svg></span><div class="txt"><b>Drains</b><small>Overdue 10 December 2023</small></div><span class="go"><svg class="ic"><use href="#i-chev"/></svg></span></div>
    <div class="row"><span class="tile warn"><svg class="ic"><use href="#i-help"/></svg></span><div class="txt"><b>Gutters</b><small>-</small></div><span class="go"><svg class="ic"><use href="#i-chev"/></svg></span></div>
  </div>
  <nav class="tabs">
    <span class="on"><svg class="ic"><use href="#i-home"/></svg>Home</span>
    <span><svg class="ic"><use href="#i-pie"/></svg>Overview</span>
    <span><svg class="ic"><use href="#i-coin"/></svg>Finances</span>
    <span><svg class="ic"><use href="#i-mail"/></svg>Messages</span>
  </nav>
</section>

<!-- Option one: finances -->
<section class="phone" style="left:220px;top:157px;width:110px;height:195px">
  <div class="status"><span>12:30PM</span><span class="sys"><i style="width:2.5px;height:2.5px"></i><i style="width:2.5px;height:2.5px;border-radius:50%"></i><i style="width:4px;height:2.2px"></i></span></div>
  <header class="bar"><svg class="ic"><use href="#i-back"/></svg><h2>Finances</h2></header>
  <div class="pbody" style="background:var(--canvas);padding-top:1px">
    <h3 class="sec">Accounts Receivable</h3>
    <div class="group"><div class="ghead"><span>Arrears</span><span class="go"><svg class="ic"><use href="#i-x"/></svg></span></div>
      <div class="stats"><div class="stat"><svg class="ic"><use href="#i-cash"/></svg><div><small>Total</small><strong>£7,268.22</strong></div></div><div class="stat"><svg class="ic"><use href="#i-doc"/></svg><div><small>Bills</small><strong>5</strong></div></div></div></div>
    <div class="group"><div class="ghead"><span>Unallocated Receipts</span><span class="go"><svg class="ic"><use href="#i-x"/></svg></span></div>
      <div class="stats"><div class="stat"><svg class="ic"><use href="#i-cash"/></svg><div><small>Total</small><strong>£7,268.22</strong></div></div><div class="stat"><svg class="ic"><use href="#i-doc"/></svg><div><small>Receipts</small><strong>5</strong></div></div></div></div>
    <h3 class="sec" style="margin-top:5px">Accounts Payable</h3>
    <div class="group"><div class="ghead"><span>Invoices</span><span class="go"><svg class="ic"><use href="#i-x"/></svg></span></div>
      <div class="stats"><div class="stat"><svg class="ic"><use href="#i-cash"/></svg><div><small>Total</small><strong>£4,268.78</strong></div></div><div class="stat"><svg class="ic"><use href="#i-doc"/></svg><div><small>Invoices</small><strong>5</strong></div></div></div></div>
  </div>
</section>

<!-- Option one: legionellas -->
<section class="phone" style="left:351px;top:157px;width:110px;height:195px">
  <div class="status"><span>12:30PM</span><span class="sys"><i style="width:2.5px;height:2.5px"></i><i style="width:2.5px;height:2.5px;border-radius:50%"></i><i style="width:4px;height:2.2px"></i></span></div>
  <header class="bar"><svg class="ic"><use href="#i-back"/></svg><h2>Legionellas</h2></header>
  <div class="pbody">
    <h3 class="q">Is it required?</h3>
    <div class="opt"><span class="radio"></span>No</div>
    <div class="opt"><span class="radio"></span>Yes, but i do not have a  file to upload</div>
    <div class="opt"><span class="radio on"><svg class="ic"><use href="#i-tick"/></svg></span>Yes, and i have a file to upload</div>
  </div>
  <div class="btns"><span class="btn">Back</span><span class="btn primary">Next</span></div>
</section>

<!-- Option two: development overview -->
<section class="phone blue" style="left:562px;top:157px;width:110px;height:279px">
  <div class="bluehead">
    <div class="status"><span>12:30PM</span><span class="sys"><i style="width:2.5px;height:2.5px"></i><i style="width:2.5px;height:2.5px;border-radius:50%"></i><i style="width:4px;height:2.2px"></i></span></div>
    <header class="bar"><span class="back"><svg class="ic"><use href="#i-back"/></svg></span><h2>Development Overview</h2></header>
  </div>
  <div class="pbody">
    <h3 class="sec">General</h3>
    <div class="grid2">
      <div class="gcard"><span class="tile"><svg class="ic"><use href="#i-cal"/></svg></span><b>Handover Date</b><small>12 January 2023</small><span class="go"><svg class="ic"><use href="#i-chev"/></svg></span></div>
      <div class="gcard"><span class="tile"><svg class="ic"><use href="#i-layers"/></svg></span><b>Units</b><small>85</small><span class="go"><svg class="ic"><use href="#i-chev"/></svg></span></div>
      <div class="gcard"><span class="tile"><svg class="ic"><use href="#i-pin"/></svg></span><b>Address</b><small>24 Alder Row, Northfield, NF2 8QA</small><span class="go"><svg class="ic"><use href="#i-chev"/></svg></span></div>
      <div class="gcard"><span class="tile"><svg class="ic"><use href="#i-bank"/></svg></span><b>Section 20 Unit</b><small>£ 20</small><span class="go"><svg class="ic"><use href="#i-chev"/></svg></span></div>
    </div>
    <h3 class="sec" style="margin-top:8px">Compliance</h3>
    <div class="grid2">
      <div class="gcard"><span class="tile"><svg class="ic"><use href="#i-doc"/></svg></span><b>Asbestos</b><small>NA</small><span class="go"><svg class="ic"><use href="#i-chev"/></svg></span></div>
      <div class="gcard"><span class="tile warn"><svg class="ic"><use href="#i-help"/></svg></span><b>EICR</b><small></small><span class="go"><svg class="ic"><use href="#i-chev"/></svg></span></div>
      <div class="gcard"><span class="tile red"><svg class="ic"><use href="#i-alert"/></svg></span><b>Drains</b><small>Overdue 10 December 2023</small><span class="go"><svg class="ic"><use href="#i-chev"/></svg></span></div>
      <div class="gcard"><span class="tile warn"><svg class="ic"><use href="#i-help"/></svg></span><b>Gutters</b><small></small><span class="go"><svg class="ic"><use href="#i-chev"/></svg></span></div>
    </div>
  </div>
  <nav class="navicons">
    <span class="on"><svg class="ic"><use href="#i-home"/></svg></span>
    <svg class="ic"><use href="#i-pie"/></svg>
    <svg class="ic"><use href="#i-coin"/></svg>
    <svg class="ic"><use href="#i-mail"/></svg>
  </nav>
</section>

<!-- Option two: finances -->
<section class="phone blue" style="left:712px;top:157px;width:109px;height:217px">
  <div class="bluehead">
    <div class="status"><span>12:30PM</span><span class="sys"><i style="width:2.5px;height:2.5px"></i><i style="width:2.5px;height:2.5px;border-radius:50%"></i><i style="width:4px;height:2.2px"></i></span></div>
    <header class="bar"><span class="back"><svg class="ic"><use href="#i-back"/></svg></span><h2>Finances</h2></header>
  </div>
  <div class="pbody">
    <h3 class="sec">Accounts Receivable</h3>
    <div class="group"><div class="ghead"><span>Arrears</span><span class="go"><svg class="ic"><use href="#i-x"/></svg></span></div>
      <div class="stats"><div class="stat col"><span class="top"><svg class="ic"><use href="#i-bank"/></svg><small>Total</small></span><strong>£7,268.22</strong></div><div class="stat col"><span class="top"><svg class="ic"><use href="#i-doc"/></svg><small>Bills</small></span><strong>5</strong></div></div></div>
    <div class="group"><div class="ghead"><span>Unallocated Receipts</span><span class="go"><svg class="ic"><use href="#i-x"/></svg></span></div>
      <div class="stats"><div class="stat col"><span class="top"><svg class="ic"><use href="#i-bank"/></svg><small>Total</small></span><strong>£7,268.22</strong></div><div class="stat col"><span class="top"><svg class="ic"><use href="#i-doc"/></svg><small>Bills</small></span><strong>5</strong></div></div></div>
    <h3 class="sec" style="margin-top:5px">Accounts Payable</h3>
    <div class="group"><div class="ghead"><span>Invoices</span><span class="go"><svg class="ic"><use href="#i-x"/></svg></span></div>
      <div class="stats"><div class="stat col"><span class="top"><svg class="ic"><use href="#i-bank"/></svg><small>Total</small></span><strong>£7,268.22</strong></div><div class="stat col"><span class="top"><svg class="ic"><use href="#i-doc"/></svg><small>Invoices</small></span><strong>10</strong></div></div></div>
  </div>
</section>

<!-- Option two: legionellas -->
<section class="phone blue" style="left:861px;top:157px;width:109px;height:195px">
  <div class="bluehead">
    <div class="status"><span>12:30PM</span><span class="sys"><i style="width:2.5px;height:2.5px"></i><i style="width:2.5px;height:2.5px;border-radius:50%"></i><i style="width:4px;height:2.2px"></i></span></div>
    <header class="bar"><span class="back"><svg class="ic"><use href="#i-back"/></svg></span><h2>Legionellas</h2></header>
  </div>
  <div class="pbody">
    <h3 class="q">Is it required?</h3>
    <div class="opt2"><svg class="mark"><use href="#i-no"/></svg>No<span class="radio"></span></div>
    <div class="opt2" style="min-height:20px"><svg class="mark"><use href="#i-file-y"/></svg>Yes, but i do not have a<br>file to upload<span class="radio on"><svg class="ic"><use href="#i-tick"/></svg></span></div>
    <div class="opt2"><svg class="mark"><use href="#i-file-b"/></svg>Yes, and i have a file to upload<span class="radio"></span></div>
  </div>
  <div class="btns"><span class="btn">Back</span><span class="btn primary">Next</span></div>
</section>

<!-- Web: overview, collapsed rail -->
<section class="tab" style="left:96px;top:548px;width:370px;height:313px">
  <header class="top">
    <svg class="ic menu-btn"><use href="#i-menu"/></svg><span class="brand" style="margin-left:9px">Hestia</span>
    <div class="user"><span class="bell"><svg class="ic"><use href="#i-bell"/></svg></span><span class="avatar" role="img" aria-label="Profile photo of the account holder"></span><span class="who"><b>Clara Westbrook</b><small>My Account</small></span></div>
  </header>
  <div class="body">
    <aside class="rail">
      <span class="act"><svg class="ic"><use href="#i-user"/></svg></span>
      <svg class="ic"><use href="#i-refresh"/></svg>
      <svg class="ic"><use href="#i-gear"/></svg>
      <svg class="ic"><use href="#i-building"/></svg>
      <svg class="ic"><use href="#i-mail"/></svg>
      <svg class="ic"><use href="#i-doc"/></svg>
      <svg class="ic end"><use href="#i-logout"/></svg>
    </aside>
    <main class="main">
      <div class="ovhead"><h2>Overview</h2><span class="report">Report</span></div>
      <div class="banner">
        <div class="notice"><i></i>Please complete basic setup</div>
        <div class="chips">
          <span class="chip">Service Charges Schedules<svg class="ic"><use href="#i-chev"/></svg></span>
          <span class="chip">Service Charges Appointment<svg class="ic"><use href="#i-chev"/></svg></span>
          <span class="chip">Invite Residents &amp; Leaseholds<svg class="ic"><use href="#i-chev"/></svg></span>
          <span class="chip">Connect Payment Holder<svg class="ic"><use href="#i-chev"/></svg></span>
        </div>
      </div>
      <div class="tabsbar"><span class="pill">Summery</span><span>Details</span></div>
      <div class="block"><h4>General</h4><div class="cells">
        <div class="cell"><span class="lab"><svg class="ic"><use href="#i-layers"/></svg>Unit<span class="go"><svg class="ic"><use href="#i-chev"/></svg></span></span><span class="val">85</span></div>
        <div class="cell"><span class="lab"><svg class="ic"><use href="#i-cal"/></svg>Handover Date<span class="go"><svg class="ic"><use href="#i-chev"/></svg></span></span><span class="val">12 January 2024</span></div>
        <div class="cell"><span class="lab"><svg class="ic"><use href="#i-pin"/></svg>Address<span class="go"><svg class="ic"><use href="#i-chev"/></svg></span></span><span class="val">24 Alder Row, Northfield, NF2 8QA</span></div>
        <div class="cell"><span class="lab"><svg class="ic"><use href="#i-cash"/></svg>Section 20 limit</span><span class="val">£ 20</span></div>
      </div></div>
      <div class="block"><h4>Compliance</h4><div class="cells">
        <div class="cell"><span class="lab"><svg class="ic"><use href="#i-doc"/></svg>Asbestos</span><span class="val">NA</span></div>
        <div class="cell"><span class="lab"><svg class="ic"><use href="#i-drop"/></svg>Legionellas</span><span class="val">NA</span></div>
        <div class="cell"><span class="lab"><svg class="ic"><use href="#i-bank"/></svg>Drains</span><span class="val">Overdue  10 Dec 2023</span></div>
        <div class="cell"><span class="lab"><svg class="ic"><use href="#i-tick"/></svg>Gutters</span><span class="val">NA</span></div>
        <div class="cell"><span class="lab"><svg class="ic"><use href="#i-wrench"/></svg>Dry Risers</span><span class="val">NA</span></div>
      </div></div>
      <div class="block"><h4>Insurance</h4><div class="cells">
        <div class="cell"><span class="lab"><svg class="ic"><use href="#i-drop"/></svg>Terrorism</span><span class="val">NA</span></div>
        <div class="cell"><span class="lab"><svg class="ic"><use href="#i-building"/></svg>Buildings</span><span class="val">NA</span></div>
        <div class="cell"><span class="lab"><svg class="ic"><use href="#i-bank"/></svg>Engineering</span><span class="val">NA</span></div>
        <div class="cell"><span class="lab"><svg class="ic"><use href="#i-ruler"/></svg>D &amp; O</span><span class="val">NA</span></div>
        <div class="cell"><span class="lab"><svg class="ic"><use href="#i-refresh"/></svg>Reinstatement</span><span class="val">NA</span></div>
      </div></div>
      <div class="block"><h4>Service Charge</h4><div class="cells fixed">
        <div class="cell"><span class="lab"><svg class="ic"><use href="#i-cal"/></svg>Year End</span><span class="val">NA</span></div>
        <div class="cell"><span class="lab"><svg class="ic"><use href="#i-cal"/></svg>Demand Dates</span><span class="val">NA</span></div>
      </div></div>
      <div class="block"><h4>Cosec</h4><div class="cells fixed">
        <div class="cell"><span class="lab"><svg class="ic"><use href="#i-key"/></svg>Are we responsible?</span><span class="val">No</span></div>
      </div></div>
    </main>
  </div>
</section>

<!-- Web: overview, open menu -->
<section class="tab" style="left:514px;top:546px;width:370px;height:304px">
  <header class="top">
    <div class="sidehead" style="width:67px"><svg class="ic"><use href="#i-menu"/></svg>Menu<svg class="ic close"><use href="#i-x"/></svg></div>
    <span class="brand">Hestia</span>
    <div class="user"><span class="bell"><svg class="ic"><use href="#i-bell"/></svg></span><span class="avatar" role="img" aria-label="Profile photo of the account holder"></span><span class="who"><b>Clara Westbrook</b><small>My Account</small></span></div>
  </header>
  <div class="body">
    <nav class="menu">
      <a class="on"><svg class="ic"><use href="#i-user"/></svg>User Directory</a>
      <a><svg class="ic"><use href="#i-refresh"/></svg>Switch Development</a>
      <a><svg class="ic"><use href="#i-gear"/></svg>Service Change</a>
      <a><svg class="ic"><use href="#i-building"/></svg>Property Balance</a>
      <a><svg class="ic"><use href="#i-mail"/></svg>Sending Letter</a>
      <a><svg class="ic"><use href="#i-doc"/></svg>Regular Services</a>
      <a class="end"><svg class="ic"><use href="#i-logout"/></svg>Logout</a>
    </nav>
    <main class="main">
      <div class="ovhead"><h2>Overview</h2><span class="report">Report</span></div>
      <div class="banner">
        <div class="notice"><i></i>Please complete basic setup</div>
        <div class="chips">
          <span class="chip">Service Charges Schedules<svg class="ic"><use href="#i-chev"/></svg></span>
          <span class="chip">Service Charges Appointment<svg class="ic"><use href="#i-chev"/></svg></span>
          <span class="chip">Invite Residents &amp; Leaseholds<svg class="ic"><use href="#i-chev"/></svg></span>
          <span class="chip">Connect Payment Holder<svg class="ic"><use href="#i-chev"/></svg></span>
        </div>
      </div>
      <div class="tabsbar"><span class="pill">Summery</span><span>Details</span></div>
      <div class="block"><h4>General</h4><div class="cells">
        <div class="cell"><span class="lab"><svg class="ic"><use href="#i-layers"/></svg>Unit<span class="go"><svg class="ic"><use href="#i-chev"/></svg></span></span><span class="val">85</span></div>
        <div class="cell"><span class="lab"><svg class="ic"><use href="#i-cal"/></svg>Handover Date<span class="go"><svg class="ic"><use href="#i-chev"/></svg></span></span><span class="val">12 January 2024</span></div>
        <div class="cell"><span class="lab"><svg class="ic"><use href="#i-pin"/></svg>Address<span class="go"><svg class="ic"><use href="#i-chev"/></svg></span></span><span class="val" style="font-size:2.9px">24 Alder Row, Northfield, NF2 8QA</span></div>
        <div class="cell"><span class="lab"><svg class="ic"><use href="#i-cash"/></svg>Section 20 limit</span><span class="val">£ 20</span></div>
      </div></div>
      <div class="block"><h4>Compliance</h4><div class="cells">
        <div class="cell"><span class="lab"><svg class="ic"><use href="#i-doc"/></svg>Asbestos</span><span class="val">NA</span></div>
        <div class="cell"><span class="lab"><svg class="ic"><use href="#i-drop"/></svg>Legionellas</span><span class="val">NA</span></div>
        <div class="cell"><span class="lab"><svg class="ic"><use href="#i-bank"/></svg>Drains</span><span class="val">Overdue  10 Dec 2023</span></div>
        <div class="cell"><span class="lab"><svg class="ic"><use href="#i-tick"/></svg>Gutters</span><span class="val">NA</span></div>
        <div class="cell"><span class="lab"><svg class="ic"><use href="#i-wrench"/></svg>Dry Risers</span><span class="val">NA</span></div>
      </div></div>
      <div class="block"><h4>Insurance</h4><div class="cells">
        <div class="cell"><span class="lab"><svg class="ic"><use href="#i-drop"/></svg>Terrorism</span><span class="val">NA</span></div>
        <div class="cell"><span class="lab"><svg class="ic"><use href="#i-building"/></svg>Buildings</span><span class="val">NA</span></div>
        <div class="cell"><span class="lab"><svg class="ic"><use href="#i-bank"/></svg>Engineering</span><span class="val">NA</span></div>
        <div class="cell"><span class="lab"><svg class="ic"><use href="#i-ruler"/></svg>D &amp; O</span><span class="val">NA</span></div>
        <div class="cell"><span class="lab"><svg class="ic"><use href="#i-refresh"/></svg>Reinstatement</span><span class="val">NA</span></div>
      </div></div>
      <div class="block"><h4>Service Charge</h4><div class="cells fixed">
        <div class="cell"><span class="lab"><svg class="ic"><use href="#i-cal"/></svg>Year End</span><span class="val">NA</span></div>
        <div class="cell"><span class="lab"><svg class="ic"><use href="#i-cal"/></svg>Demand Dates</span><span class="val">NA</span></div>
      </div></div>
      <div class="block"><h4>Cosec</h4><div class="cells fixed">
        <div class="cell"><span class="lab"><svg class="ic"><use href="#i-key"/></svg>Are we responsible?</span><span class="val">No</span></div>
      </div></div>
    </main>
  </div>
</section>

<!-- Web: finances, open menu -->
<section class="tab" style="left:96px;top:887px;width:370px;height:223px">
  <header class="top">
    <div class="sidehead" style="width:57px;border-right:0"><svg class="ic"><use href="#i-menu"/></svg>Menu<svg class="ic close"><use href="#i-x"/></svg></div>
    <span class="brand">Hestia</span>
    <div class="user"><span class="bell"><svg class="ic"><use href="#i-bell"/></svg></span><span class="avatar" role="img" aria-label="Profile photo of the account holder"></span><span class="who"><b>Clara Westbrook</b><small>Development Manager</small></span></div>
  </header>
  <div class="body">
    <nav class="menu long" style="width:57px">
      <a><svg class="ic"><use href="#i-home"/></svg>Home</a>
      <a><svg class="ic"><use href="#i-bell"/></svg>Announcement</a>
      <a><svg class="ic"><use href="#i-bank"/></svg>Bank Balance</a>
      <a><svg class="ic"><use href="#i-doc"/></svg>Billing</a>
      <a><svg class="ic"><use href="#i-folder"/></svg>Directory</a>
      <a><svg class="ic"><use href="#i-doc"/></svg>Documents</a>
      <a><svg class="ic"><use href="#i-coin"/></svg>Ground Rent</a>
      <a><svg class="ic"><use href="#i-bell"/></svg>Notifications</a>
      <a><svg class="ic"><use href="#i-mail"/></svg>Messages</a>
      <a><svg class="ic"><use href="#i-cal"/></svg>Packages</a>
      <a><svg class="ic"><use href="#i-building"/></svg>Property Balance</a>
      <a><svg class="ic"><use href="#i-gear"/></svg>Service Charge</a>
      <a><svg class="ic"><use href="#i-gear"/></svg>Settings</a>
      <a><svg class="ic"><use href="#i-cash"/></svg>Tickets</a>
      <a><svg class="ic"><use href="#i-logout"/></svg>Logout</a>
    </nav>
    <main class="main fin">
      <h2>Finances</h2>
      <div class="fcards">
        <div class="fcard"><svg class="ic"><use href="#i-user"/></svg>Sub Account<span class="go"><svg class="ic"><use href="#i-chev"/></svg></span></div>
        <div class="fcard"><svg class="ic"><use href="#i-globe"/></svg>Payment Provider<span class="foot"><span class="ok">Connected</span><span class="go"><svg class="ic"><use href="#i-chev"/></svg></span></span></div>
      </div>
    </main>
  </div>
</section>

<!-- Web: finances, collapsed rail -->
<section class="tab" style="left:514px;top:887px;width:370px;height:223px">
  <header class="top">
    <svg class="ic menu-btn" style="margin-left:8px"><use href="#i-menu"/></svg><span class="brand" style="margin-left:16px">Hestia</span>
    <div class="user"><span class="bell"><svg class="ic"><use href="#i-bell"/></svg></span><span class="avatar" role="img" aria-label="Profile photo of the account holder"></span><span class="who"><b>Clara Westbrook</b><small>Development Manager</small></span></div>
  </header>
  <div class="body">
    <aside class="rail tall">
      <svg class="ic"><use href="#i-home"/></svg>
      <svg class="ic"><use href="#i-bell"/></svg>
      <svg class="ic"><use href="#i-bank"/></svg>
      <svg class="ic"><use href="#i-doc"/></svg>
      <svg class="ic"><use href="#i-folder"/></svg>
      <svg class="ic"><use href="#i-doc"/></svg>
      <svg class="ic"><use href="#i-coin"/></svg>
      <svg class="ic"><use href="#i-bell"/></svg>
      <svg class="ic"><use href="#i-mail"/></svg>
      <svg class="ic"><use href="#i-cal"/></svg>
      <svg class="ic"><use href="#i-building"/></svg>
      <svg class="ic"><use href="#i-gear"/></svg>
      <svg class="ic"><use href="#i-gear"/></svg>
      <svg class="ic"><use href="#i-cash"/></svg>
      <svg class="ic"><use href="#i-logout"/></svg>
    </aside>
    <main class="main fin">
      <h2 style="margin-top:4px">Finances</h2>
      <div class="fchips">
        <div class="fchip"><svg class="ic"><use href="#i-user"/></svg>Sub Account<span class="go"><svg class="ic"><use href="#i-chev"/></svg></span></div>
        <div class="fchip"><svg class="ic"><use href="#i-globe"/></svg>Payment Provider<span class="ok">Connected</span><span class="go"><svg class="ic"><use href="#i-chev"/></svg></span></div>
      </div>
    </main>
  </div>
</section>

</body>
</html>
```